Gordon Pellbrook Consulting - Web Design Project

We need a web design for my new edgy consulting business specializing in innovation, technology and strategy.

It is our personal goal to turn each client into raving fans by helping them achieve their own business goals and aspirations through assisting them in raising their own innovation and marketing standards.

We provide our personalised and state-of-the-art services to our clients and boards who represent some of the world greatest innovative thinkers.
Updates

Here is some other information which may help shape your thinking.

I've had direct Involvement in the development of the following iPad, iPhone Applications and websites

FarbeyondOzlands.com (TerraLink platform) by Voyage Bureau
http://farbeyondozlands.example.au

Sail Verve by Bright Voyaging
https://apps.example-store.com/au/app/sail-verve/id100000001

uRedlandTR by Travel Territory Board
https://apps.example-store.com/au/app/uredlandtr/id100000002

Wexmoor Trips
http://www.wexmoortrips.example.au

Trek Mapper by Voyage Bureau
http://apps.example-store.com/au/app/trek-mapper/id100000003

Sunward by Sunward Travel Office
https://apps.example-store.com/au/app/sunward/id100000004

Upper Fernridge Valley Route by Visit Coastlands
https://apps.example-store.com/au/app/upper-fernridge-valley-route/id100000005

Wanderer Path by Travel Territory Board and Southern Plains Travel Council
https://apps.example-store.com/au/app/wanderers-path-grand-journey/id100000006

Gordon Pellbrook Consulting (GPC)
November 2012 – Present (8 months)Brisbane, Sydney, Canberra

Gordon’s consults to Small-to-Medium Enterprises (SME) and Government organisations on business strategy, technology strategy, risk mitigation, disruptive technology and innovation in the workplace.

Gordon’s consultancy mantra is that we cannot divorce economic life from cultural life particularly in an era when social capital may be as important as physical capital in business.

Reason: request from designers, I want to see their best efforts

Target Market(s)

35+

Industry/Entity Type

Business

Requirements
Must have
• Please use some of the personal image(s) contained in the zip files which can be downloaded from here

http://filedrop.example/k9Xq2Lm
http://filedrop.example/p4Rt7Vn
http://filedrop.example/z8Hw3Bc
Nice to have
• Black, Sleek design, maybe minimalist. Nice to have a Pixelle for the design. Nice to have it easily ported to Wordpress or be a modified Wordpress template. HTML 5, responsive design

```html
<!DOCTYPE html>
<html lang="en">
<head>
<meta charset="utf-8">
<title>Gordon Pellbrook Consulting</title>
<link rel="stylesheet" href="https://fonts.googleapis.com/css2?family=Questrial&family=Arimo:wght@400;700&family=Anton&display=swap">
<style>
  :root {
    --gold: #8a6510;
    --gold-bright: #a67c1a;
    --ink: #1f1f1f;
    --header-top: #1a1a1a;
    --header-bottom: #2b2b2b;
    --hero-top: #2a2929;
    --hero-bottom: #3d3c3c;
    --tile-light: #e9e9e9;
    --tile-dark: #c3c3c3;
    --tile-text: #4a4a4a;
    --muted: #8f8f8f;
    --heading: #8c8c8c;
    --white: #ffffff;
    --footer-text: #2a1f05;
  }
  * { margin: 0; padding: 0; box-sizing: border-box; }
  html, body { width: 1200px; height: 1000px; overflow: hidden; background: var(--ink); }
  .page { position: relative; width: 1200px; height: 1000px; background: var(--ink); font-family: "Arimo", Arial, sans-serif; }

  .site-header { position: absolute; left: 0; top: 0; width: 1200px; height: 108px;
    background: linear-gradient(var(--header-top), var(--header-bottom)); }
  .brand { position: absolute; left: 224px; top: 20px; font-family: "Questrial", sans-serif; color: var(--white); font-weight: 400; }
  .brand-name { display: block; font-size: 32px; line-height: 36px; letter-spacing: 0.5px; }
  .brand-tag { display: block; font-size: 19px; line-height: 20px; letter-spacing: 8.4px; }

  .main-nav { position: absolute; right: 220px; top: 70px; display: flex; gap: 11px;
    font-family: "Questrial", sans-serif; font-size: 17px; letter-spacing: 1.3px; }
  .main-nav a { color: var(--white); text-decoration: none; }
  .main-nav a.is-active { color: var(--gold-bright); }
  .nav-marker { position: absolute; left: 669px; top: 96px; }

  .gold-band { position: absolute; left: 0; top: 108px; width: 1200px; height: 66px; background: var(--gold); }
  .hero { position: absolute; left: 0; top: 174px; width: 1200px; height: 297px;
    background: linear-gradient(#262525, var(--hero-top) 12%, var(--hero-bottom)); }
  .hero-portrait { position: absolute; left: 222px; top: 128px; width: 218px; height: 343px;
    background: linear-gradient(#3a3a44, #1d1d26); border-radius: 80px 80px 0 0; }
  .hero-quote { position: absolute; left: 440px; top: 200px; width: 550px; text-align: center;
    color: var(--white); font-weight: 700; text-shadow: 2px 3px 4px rgba(0,0,0,0.6); }
  .hero-quote .lead { display: block; font-size: 66px; line-height: 76px; letter-spacing: 3px; }
  .hero-quote .line { display: block; font-size: 31px; line-height: 38px; letter-spacing: 2.6px; }
  .hero-quote .close { display: block; font-size: 30px; line-height: 26px; }
  .slider-dots { position: absolute; left: 918px; top: 448px; display: flex; gap: 8px; }
  .slider-dots span { width: 12px; height: 12px; border-radius: 50%; background: var(--gold); }

  .services-band { position: absolute; left: 0; top: 471px; width: 1200px; height: 132px; background: var(--gold); }
  .services { position: absolute; left: 196px; top: 471px; display: flex; height: 132px; }
  .service-tile { position: relative; height: 132px; padding: 6px 0 0 11px;
    font-family: "Anton", Impact, sans-serif; font-size: 50px; line-height: 44px; color: var(--tile-text); letter-spacing: -0.5px; }
  .service-tile.light { background: var(--tile-light); }
  .service-tile.dark { background: var(--tile-dark); }
  .service-tile svg { position: absolute; right: 8px; bottom: 7px; }

  .section-title { font-size: 26px; font-weight: 700; color: var(--heading); line-height: 30px;
    padding-bottom: 10px; border-bottom: 3px solid var(--gold); }
  .welcome { position: absolute; left: 202px; top: 622px; width: 386px; }
  .welcome p { margin-top: 16px; font-size: 12.4px; line-height: 13.5px; color: var(--muted); text-align: justify; }
  .news { position: absolute; left: 606px; top: 622px; width: 385px; }
  .news ul { list-style: none; margin-top: 12px; padding-left: 10px; }
  .news li { position: relative; padding-left: 24px; margin-bottom: 4px; font-size: 16px; line-height: 20px; }
  .news li a { color: var(--heading); text-decoration: underline; text-underline-offset: 3px; }
  .news li svg { position: absolute; left: 0; top: 5px; }
  .read-more { position: absolute; right: 12px; top: 176px; display: flex; align-items: center; gap: 8px;
    color: var(--heading); font-size: 17px; text-decoration: none; }
  .read-more span.box { width: 28px; height: 26px; background: #9a9a9a; display: flex; align-items: center; justify-content: center; }

  .site-footer { position: absolute; left: 0; top: 968px; width: 1200px; height: 32px; background: var(--gold);
    font-size: 11px; font-weight: 700; color: var(--footer-text); }
  .footer-links { position: absolute; left: 202px; top: 10px; }
  .footer-links a { color: var(--footer-text); text-decoration: none; }
  .copyright { position: absolute; right: 209px; top: 10px; font-weight: 400; }
</style>
</head>
<body>
<div class="page">
  <header class="site-header">
    <div class="brand">
      <span class="brand-name">Gordon Pellbrook</span>
      <span class="brand-tag">CONSULTING</span>
    </div>
    <nav class="main-nav">
      <a class="is-active" href="#">HOME</a>
      <a href="#">ABOUT</a>
      <a href="#">SERVICES</a>
      <a href="#">CONTACT</a>
    </nav>
  </header>
  <svg class="nav-marker" width="28" height="13" viewBox="0 0 28 13"><polygon points="0,13 14,0 28,13" fill="#8a6510"/></svg>

  <div class="gold-band"></div>
  <section class="hero">
    <div class="slider-dots" style="left:918px;top:274px"><span></span><span></span><span></span></div>
  </section>
  <div class="hero-portrait" role="img" aria-label="Portrait of Gordon Pellbrook in a dark suit"></div>
  <h1 class="hero-quote">
    <span class="lead">“LOREM IPSUM</span>
    <span class="line">this text can be changed</span>
    <span class="line">IT’S CAN BE YOUR SERVICE</span>
    <span class="close">”</span>
  </h1>

  <div class="services-band"></div>
  <div class="services">
    <a class="service-tile light" style="width:201px">CONSU<br>LTING
      <svg width="38" height="38" viewBox="0 0 38 38"><circle cx="19" cy="19" r="17" fill="none" stroke="#3a3a3a" stroke-width="3"/><path d="M10 19h15M19 11l8 8-8 8" fill="none" stroke="#3a3a3a" stroke-width="4"/></svg></a>
    <a class="service-tile dark" style="width:201px">RESEA<br>RCH
      <svg width="38" height="38" viewBox="0 0 38 38"><circle cx="19" cy="19" r="17" fill="none" stroke="#3a3a3a" stroke-width="3"/><path d="M10 19h15M19 11l8 8-8 8" fill="none" stroke="#3a3a3a" stroke-width="4"/></svg></a>
    <a class="service-tile light" style="width:197px">ANALY<br>SYS
      <svg width="38" height="38" viewBox="0 0 38 38"><circle cx="19" cy="19" r="17" fill="none" stroke="#3a3a3a" stroke-width="3"/><path d="M10 19h15M19 11l8 8-8 8" fill="none" stroke="#3a3a3a" stroke-width="4"/></svg></a>
    <a class="service-tile dark" style="width:201px">TRAIN<br>ING
      <svg width="38" height="38" viewBox="0 0 38 38"><circle cx="19" cy="19" r="17" fill="none" stroke="#3a3a3a" stroke-width="3"/><path d="M10 19h15M19 11l8 8-8 8" fill="none" stroke="#3a3a3a" stroke-width="4"/></svg></a>
  </div>

  <section class="welcome">
    <h2 class="section-title">Welcome!</h2>
    <p>Lorem ipsum dolor sit amet, consectetur adipisicing elit, sed do eiusmod tempor incididunt ut labore et dolore magna aliqua. Ut enim ad minim veniam, quis nostrud exercitation ullamco laboris nisi ut aliquip ex ea commodo consequat. Duis aute irure dolor in reprehenderit in voluptate velit esse cillum dolore eu fugiat nulla pariatur. Excepteur sint occaecat cupidatat non proident, sunt in culpa qui officia deserunt mollit anim id est laborum.<br>Lorem ipsum dolor sit amet, consectetur adipisicing elit, sed do eiusmod tempor incididunt ut labore et dolore magna aliqua. Ut enim ad minim veniam, quis nostrud exercitation ullamco laboris nisi...</p>
  </section>

  <section class="news">
    <h2 class="section-title">Latest News</h2>
    <ul>
      <li><svg width="16" height="10" viewBox="0 0 16 10"><path d="M1 1l5 4-5 4M7 1l5 4-5 4" fill="none" stroke="#aaa" stroke-width="1.5"/></svg><a href="#">Lorem Ipsum this is the title and it is a link</a></li>
      <li><svg width="16" height="10" viewBox="0 0 16 10"><path d="M1 1l5 4-5 4M7 1l5 4-5 4" fill="none" stroke="#aaa" stroke-width="1.5"/></svg><a href="#">Lorem Ipsum this is the title and it is a link and this is two lines</a></li>
      <li><svg width="16" height="10" viewBox="0 0 16 10"><path d="M1 1l5 4-5 4M7 1l5 4-5 4" fill="none" stroke="#aaa" stroke-width="1.5"/></svg><a href="#">Maximum is two line for the title</a></li>
      <li><svg width="16" height="10" viewBox="0 0 16 10"><path d="M1 1l5 4-5 4M7 1l5 4-5 4" fill="none" stroke="#aaa" stroke-width="1.5"/></svg><a href="#">And contains of four latest news without thumb</a></li>
    </ul>
    <a class="read-more" href="#">READ MORE <span class="box"><svg width="16" height="10" viewBox="0 0 16 10"><path d="M1 1l5 4-5 4M7 1l5 4-5 4" fill="none" stroke="#ddd" stroke-width="1.5"/></svg></span></a>
  </section>

  <footer class="site-footer">
    <div class="footer-links"><a href="#">Home</a> | <a href="#">About</a> | <a href="#">FAQ</a> | <a href="#">Site Map</a></div>
    <div class="copyright">© 2012 Gordon Pellbrook | All Rights Reserved</div>
  </footer>
</div>
</body>
</html>
```